Real Estate Website

Peckford Realty will primarily be a residential rental and sales business.

Sales - Current properties - sold properties
Rentals - current properties - leased properties
Insights - Blog - Suburb profile
About us - Our agents
Working with us - rental/Sales

Here is a site that i like. Dont require video in the background.
https://www.mintowgate.com.au/
Scaled down version of this would be great. I like the landing page where it focuses on the client being vendor/landlord - not the buyers and sellers

Please make a banner on the home page that says 'request a free appraisal' with a button saying 'click here'.

I've attached some branding logos etc.
Brand colour is #f6ecd7 but using a white or black as the main of the website is fine.

```html
<!DOCTYPE html>
<html lang="en">
<head>
<meta charset="utf-8">
<title>Peckford Realty — Home</title>
<link rel="stylesheet" href="https://fonts.googleapis.com/css2?family=Oswald:wght@500;600&family=Poppins:wght@400;500;600&family=Libre+Baskerville:wght@400&display=swap">
<style>
:root{
  --ink:#0b0b0b;
  --black:#000;
  --white:#fff;
  --paper:#ffffff;
  --brand:#f6ecd7;
  --soft-ink:#33465a;
  --tab-off:#a9a9a9;
  --card-shadow:rgba(0,0,0,.12);
  --hero-cream:#e7e2d4;
  --hero-sky:#b9c7d2;
  --hero-city:#6f7f8c;
  --panel:rgba(40,40,42,.82);
  --field:rgba(70,70,72,.9);
}
*{box-sizing:border-box;margin:0;padding:0}
html,body{width:1200px;height:2938px;overflow:hidden;background:var(--paper)}
body{font-family:"Poppins",sans-serif;color:var(--ink);position:relative}
.section{position:absolute;left:0;width:1200px}
.abs{position:absolute}
.heading{font-family:"Oswald",sans-serif;font-weight:600;text-transform:uppercase;letter-spacing:1px}
.rule{position:absolute;height:2px;width:70px;background:var(--ink)}

/* Hero */
.hero{top:0;height:580px;overflow:hidden}
.hero-photo{position:absolute;inset:0;background:
  linear-gradient(90deg,var(--hero-cream) 0%,#ece8dc 38%,rgba(236,232,220,.2) 58%,transparent 75%),
  linear-gradient(180deg,#f1eee6 0%,var(--hero-sky) 45%,var(--hero-city) 78%,#d9d4c6 100%)}
.logo{font-family:"Poppins",sans-serif;font-weight:500;text-transform:uppercase;text-align:center;line-height:1;color:var(--ink)}
.logo .l1{font-size:22px;letter-spacing:3px;display:block}
.logo .l2{font-size:14px;letter-spacing:4px;display:block;margin-top:3px}
.hero .logo{left:163px;top:40px}
.nav{left:470px;top:51px;display:flex;gap:26px;font-size:11px}
.social-top{left:1007px;top:48px;display:flex;gap:12px}
.social-top span{width:15px;height:15px;border:1.6px solid var(--ink);border-radius:50%}
.dots{left:75px;top:266px;display:flex;flex-direction:column;gap:14px}
.dots span{width:11px;height:11px;border-radius:50%;background:#8d8d8d}
.dots span.on{background:var(--ink)}
.hero-copy{left:224px;top:324px}
.hero-copy .kicker{font-family:"Oswald",sans-serif;font-weight:500;font-size:18px}
.hero-copy h1{font-family:"Oswald",sans-serif;font-weight:600;font-size:50px;line-height:58px;letter-spacing:4px;margin-top:4px}
.hero-copy h1 .big{font-size:64px;letter-spacing:5px}
.hero-copy p{font-family:"Oswald",sans-serif;font-weight:500;font-size:14px;line-height:17px;width:400px;margin-top:10px}
.search{left:762px;top:315px;width:232px;height:222px;background:var(--panel);border-radius:4px;color:var(--white);padding:14px 16px}
.search h3{font-size:12px;font-weight:400}
.search .lbl{font-size:7px;text-transform:uppercase;color:#c9c9c9;position:absolute}
.search .field{position:absolute;height:30px;background:var(--field);border-radius:3px;font-size:9px;padding:9px 10px}
.search .btn{position:absolute;left:60px;top:183px;width:112px;height:32px;background:var(--black);border-radius:7px;font-size:10px;text-align:center;line-height:32px}

/* About */
.about{top:580px;height:574px}
.about-photo{left:77px;top:56px;width:411px;height:487px;background:linear-gradient(135deg,#e9e3d6 0%,#c9b48a 35%,#3c4f6d 60%,#1f2d44 85%,#7c6a54 100%)}
.about h2{left:522px;top:70px;font-size:20px}
.about .rule{left:522px;top:102px;width:62px}
.about-text{left:522px;top:120px;width:580px;font-size:12.5px;line-height:18.5px;color:var(--soft-ink);letter-spacing:.4px}
.pill{background:var(--black);color:var(--white);border-radius:8px;font-size:11px;text-align:center}
.about .pill{left:522px;top:202px;width:132px;height:32px;line-height:32px}
.offer{left:488px;top:248px;width:657px;height:295px;background:var(--black);color:var(--white)}
.offer h2{left:36px;top:22px;font-size:19px}
.offer .item{position:absolute;width:250px}
.offer .item h4{font-family:"Oswald",sans-serif;font-weight:500;font-size:14px;display:flex;align-items:center;gap:10px;letter-spacing:.5px}
.offer .item p{font-size:8.5px;line-height:15px;margin:9px 0 0 34px;color:#e6e6e6}

/* Listings */
.listings{top:1154px;height:972px}
.listings h2{left:147px;top:54px;font-size:22px}
.listings .rule{left:147px;top:90px;width:106px}
.listings .intro{left:147px;top:110px;width:900px;font-size:12px;line-height:21px;color:var(--soft-ink)}
.tabs{left:446px;top:182px;display:flex;gap:34px;font-family:"Oswald",sans-serif;font-weight:600;font-size:17px;letter-spacing:1px;text-transform:uppercase}
.tabs .off{color:var(--tab-off)}
.card{position:absolute;width:278px;height:253px;background:var(--white);box-shadow:0 3px 12px var(--card-shadow)}
.card .ph{height:183px}
.card .addr{position:absolute;left:18px;top:197px;font-family:"Libre Baskerville",serif;font-size:11px;color:#4b4b4b}
.card .meta{position:absolute;left:18px;top:226px;display:flex;align-items:center;gap:8px;font-size:9px;color:#666}
.card .meta i{width:1px;height:14px;background:#888;display:block}
.card .price{position:absolute;right:18px;top:218px;width:72px;height:28px;line-height:28px;background:var(--black);color:var(--white);border-radius:6px;text-align:center;font-size:12px;font-weight:600}
.view{width:114px;height:38px;line-height:38px;border-radius:6px;font-size:11px;text-align:center}
.listings .view{left:543px;top:808px;background:var(--black);color:var(--white);box-shadow:0 3px 8px rgba(0,0,0,.3)}
.appraisal{left:147px;top:872px;width:906px;height:72px;background:var(--brand);display:flex;align-items:center;justify-content:space-between;padding:0 36px}
.appraisal h3{font-size:20px}
.appraisal .pill{width:132px;height:36px;line-height:36px}

/* News */
.news{top:2126px;height:540px;background:var(--black);color:var(--white)}
.news h2{left:161px;top:48px;font-size:24px}
.post{position:absolute;top:117px;width:275px}
.post .ph{height:145px;position:relative}
.post .date{position:absolute;right:0;bottom:0;width:38px;height:38px;background:var(--black);font-size:8px;font-weight:600;text-align:center;line-height:11px;padding-top:8px}
.post .cat{font-size:8px;font-weight:600;margin:14px 0 0 12px;text-transform:uppercase}
.post h3{font-family:"Libre Baskerville",serif;font-weight:400;font-size:14px;margin-top:16px}
.post .by{font-size:8px;margin-top:4px}
.post p{font-size:8px;line-height:13px;margin-top:8px;color:#e0e0e0}
.post .more{display:inline-block;margin-top:15px;border:1.5px solid var(--white);border-radius:5px;font-size:8px;font-weight:600;padding:5px 14px;text-transform:uppercase}
.news .view{left:543px;top:462px;border:1.5px solid var(--white)}

/* Footer */
.footer{top:2666px;height:272px}
.footer .line{position:absolute;left:147px;width:906px;height:1px;background:#555}
.footer .logo{left:147px;top:66px}
.fcol{position:absolute;top:66px;font-size:9px;color:#555}
.fcol h5{font-size:9.5px;font-weight:500;color:var(--ink)}
.fcol .dash{width:18px;height:1.5px;background:var(--ink);margin:12px 0 12px}
.fcol li{list-style:none;line-height:20px}
.subscribe{left:795px;top:104px;display:flex;width:259px;height:32px;border:1px solid #999}
.subscribe .in{flex:1;font-size:8.5px;color:#888;padding:10px}
.subscribe .go{width:78px;background:var(--black);color:var(--white);font-size:9px;text-align:center;line-height:30px}
.social-foot{left:147px;top:140px;display:flex;gap:10px}
.social-foot span{width:27px;height:27px;border:1.3px solid var(--ink);border-radius:50%}
.copyright{left:0;width:1200px;top:246px;text-align:center;font-size:9px;color:#555}
</style>
</head>
<body>

<header class="section hero">
  <div class="hero-photo" role="img" aria-label="Bright penthouse interior with tall angled windows overlooking a city skyline"></div>
  <div class="abs logo"><span class="l1">Peckford</span><span class="l2">Realty</span></div>
  <nav class="abs nav"><span>Home</span><span>Sales</span><span>Rentals</span><span>Insights</span><span>About us</span><span>Working with us</span></nav>
  <div class="abs social-top" aria-label="Social links"><span></span><span></span><span></span></div>
  <div class="abs dots"><span></span><span class="on"></span><span></span></div>
  <div class="abs hero-copy">
    <div class="kicker">Peckford Realty</div>
    <h1>The Real Estate<br><span class="big">Market Place</span></h1>
    <p>Lorem Ipsum is simply dummy text of the printing and typesetting industry.</p>
  </div>
  <form class="abs search">
    <h3>Reserve The Villa Now</h3>
    <span class="lbl" style="left:16px;top:62px">Looking for</span>
    <span class="lbl" style="left:120px;top:62px">City</span>
    <div class="field" style="left:16px;top:76px;width:96px">Rent House
      <svg style="position:absolute;right:8px;top:12px" width="8" height="5" viewBox="0 0 8 5"><path d="M1 1l3 3 3-3" fill="none" stroke="#ccc"/></svg></div>
    <div class="field" style="left:120px;top:76px;width:96px">Brookvale</div>
    <span class="lbl" style="left:16px;top:128px">Rent price</span>
    <div class="field" style="left:16px;top:140px;width:200px">10K-20K
      <svg style="position:absolute;right:10px;top:12px" width="8" height="5" viewBox="0 0 8 5"><path d="M1 1l3 3 3-3" fill="none" stroke="#ccc"/></svg></div>
    <div class="btn">SEARCH</div>
  </form>
</header>

<section class="section about">
  <div class="abs about-photo" role="img" aria-label="Modern living room with navy feature wall, pendant lights and yellow armchair"></div>
  <h2 class="abs heading">About Us</h2>
  <div class="rule"></div>
  <p class="abs about-text">Lorem Ipsum is simply dummy text of the printing and typesetting industry. Lorem Ipsum has been the industry's standard dummy text ever since the 1500s, when an unknown printer took a galley of type and scrambled it to make a type specimen book</p>
  <div class="abs pill">Learn More</div>
  <div class="abs offer">
    <h2 class="abs heading">What We Offer</h2>
    <div class="item" style="left:34px;top:92px">
      <h4><svg width="22" height="18" viewBox="0 0 22 18" fill="none" stroke="#fff" stroke-width="1.4"><path d="M2 6l5-4 4 3 4-3 5 4-9 10z"/><path d="M7 7l4 3 4-3"/></svg>Loyalty Programs</h4>
      <p>We have partnered with vendors at a local, city, and national level to bring even more value to our tenants and communities.</p>
    </div>
    <div class="item" style="left:356px;top:92px">
      <h4><svg width="22" height="20" viewBox="0 0 22 20" fill="none" stroke="#fff" stroke-width="1.4"><circle cx="11" cy="8" r="6"/><circle cx="11" cy="8" r="2.5"/><path d="M7 13l-2 6 6-2 6 2-2-6"/></svg>20 Years Experience</h4>
      <p>We have grown from a local single-family home developer to an industry leader in building and managing housing developments across the region.</p>
    </div>
    <div class="item" style="left:34px;top:208px">
      <h4><svg width="22" height="18" viewBox="0 0 22 18" fill="none" stroke="#fff" stroke-width="1.4"><path d="M5 2h12l4 5-10 10L1 7z"/><path d="M1 7h20M8 2l3 15 3-15"/></svg>Always the Best Value</h4>
      <p>We always remain focused on upgrading and improving our buildings to ensure the satisfaction of our residents and building staff.</p>
    </div>
    <div class="item" style="left:356px;top:208px">
      <h4><svg width="22" height="20" viewBox="0 0 22 20" fill="none" stroke="#fff" stroke-width="1.4"><circle cx="11" cy="6" r="4"/><path d="M4 19c0-5 3-7 7-7s7 2 7 7z"/></svg>24 Hour customer service available</h4>
      <p>Our client care team are always there to take your call, supporting you throughout the best rental experience morning, noon or night.</p>
    </div>
  </div>
</section>

<section class="section listings">
  <h2 class="abs heading">Find Your Dream Home</h2>
  <div class="rule"></div>
  <p class="abs intro">Lorem ipsum dolor sit amet,Stet clita kasd gubergren, no sea takimata sanctus est is the lorem ipsum dolor sit amet. sed diam nonumy ut labore et dolore s the magna aliquyam.</p>
  <div class="abs tabs"><span>For Sell</span><span class="off">For Rent</span><span class="off">Sold</span></div>

  <article class="card" style="left:147px;top:240px"><div class="ph" role="img" aria-label="Reading nook with shelves and rattan chair" style="background:linear-gradient(135deg,#e8dccb,#b78b5a 55%,#5a4232)"></div>
    <div class="addr">Harbor Lane, Apt P101, Brookvale</div><div class="meta"><span>▭ 2bd</span><i></i><span>⊔ 2ba</span><i></i></div><div class="price">$6,500</div></article>
  <article class="card" style="left:461px;top:240px"><div class="ph" role="img" aria-label="Entry hall with timber staircase" style="background:linear-gradient(135deg,#c9b7a0,#8a5a38 55%,#f0e6d8)"></div>
    <div class="addr">Harbor Lane, Apt P101, Brookvale</div><div class="meta"><span>▭ 2bd</span><i></i><span>⊔ 2ba</span><i></i></div><div class="price">$6,500</div></article>
  <article class="card" style="left:775px;top:240px"><div class="ph" role="img" aria-label="Bright foyer with curved white staircase" style="background:linear-gradient(135deg,#f3eee6,#d8c6a8 55%,#8c7660)"></div>
    <div class="addr">Harbor Lane, Apt P101, Brookvale</div><div class="meta"><span>▭ 2bd</span><i></i><span>⊔ 2ba</span><i></i></div><div class="price">$6,500</div></article>

  <article class="card" style="left:147px;top:527px"><div class="ph" role="img" aria-label="Loft room with exposed brick walls" style="background:linear-gradient(135deg,#6e4a36,#b09880 55%,#d8cfc2)"></div>
    <div class="addr">Harbor Lane, Apt P101, Brookvale</div><div class="meta"><span>▭ 2bd</span><i></i><span>⊔ 2ba</span><i></i></div><div class="price">$6,500</div></article>
  <article class="card" style="left:461px;top:527px"><div class="ph" role="img" aria-label="Reading nook with shelves and rattan chair" style="background:linear-gradient(135deg,#e8dccb,#b78b5a 55%,#5a4232)"></div>
    <div class="addr">Harbor Lane, Apt P101, Brookvale</div><div class="meta"><span>▭ 2bd</span><i></i><span>⊔ 2ba</span><i></i></div><div class="price">$6,500</div></article>
  <article class="card" style="left:775px;top:527px"><div class="ph" role="img" aria-label="White modern house beside a green tree" style="background:linear-gradient(135deg,#eef0f2,#c9cfd4 50%,#3f5a34)"></div>
    <div class="addr">Harbor Lane, Apt P101, Brookvale</div><div class="meta"><span>▭ 2bd</span><i></i><span>⊔ 2ba</span><i></i></div><div class="price">$6,500</div></article>

  <div class="abs view">View All &nbsp;→</div>

  <div class="abs appraisal">
    <h3 class="heading">Request a free appraisal</h3>
    <div class="pill">Click here</div>
  </div>
</section>

<section class="section news">
  <h2 class="abs heading">Our Recent News</h2>
  <article class="post" style="left:161px">
    <div class="ph" role="img" aria-label="Swirling golden and teal smoke" style="background:linear-gradient(135deg,#1d4a3e,#c99a1a 50%,#2d3a44)"><div class="date">15<br>JULY</div></div>
    <div class="cat">Awards</div><h3>Is The Herbal Way The Right Way</h3><div class="by">by Jane Holt - April 17,2019</div>
    <p>Proin vitae nisl mauris. Nulla dignissim maximus molestie. Orci varius natoque penatibus et magnis dis parturient montes, nascetur ridiculus mus. Maecenas et mi ac ante lacinia</p>
    <span class="more">Read More</span></article>
  <article class="post" style="left:461px">
    <div class="ph" role="img" aria-label="Lone tree silhouette under a crimson sky" style="background:linear-gradient(180deg,#3a1a4a,#c2284a 55%,#2a0c1c)"><div class="date">15<br>JULY</div></div>
    <div class="cat">Local News</div><h3>Is The Herbal Way The Right Way</h3><div class="by">by Jane Holt - April 17,2019</div>
    <p>Proin vitae nisl mauris. Nulla dignissim maximus molestie. Orci varius natoque penatibus et magnis dis parturient montes, nascetur ridiculus mus. Maecenas et mi ac ante lacinia</p>
    <span class="more">Read More</span></article>
  <article class="post" style="left:762px">
    <div class="ph" role="img" aria-label="Mountain lake with a wooden boathouse" style="background:linear-gradient(180deg,#8aa0b4,#4c6a66 50%,#1f3a38)"><div class="date">15<br>JULY</div></div>
    <div class="cat">Real State</div><h3>Is The Herbal Way The Right Way</h3><div class="by">by Jane Holt - April 17,2019</div>
    <p>Proin vitae nisl mauris. Nulla dignissim maximus molestie. Orci varius natoque penatibus et magnis dis parturient montes, nascetur ridiculus mus. Maecenas et mi ac ante lacinia</p>
    <span class="more">Read More</span></article>
  <div class="abs view">View All &nbsp;→</div>
</section>

<footer class="section footer">
  <div class="line" style="top:30px"></div>
  <div class="abs logo"><span class="l1">Peckford</span><span class="l2">Realty</span></div>
  <div class="fcol" style="left:380px"><h5>Quick Links</h5><div class="dash"></div><ul><li>- Home</li><li>- About Us</li><li>- Services</li><li>- Testimonials</li><li>- Contact Us</li></ul></div>
  <div class="fcol" style="left:532px"><h5>Sitemap</h5><div class="dash"></div><ul><li>- Our Process</li><li>- What We Do</li><li>- Location</li><li>- Sell</li><li>- Purchase</li></ul></div>
  <div class="fcol" style="left:657px"><h5>Discover</h5><div class="dash"></div><ul><li>- Privacy Policy</li><li>- Terms &amp; Conditions</li><li>- Owners</li><li>- Houses</li></ul></div>
  <div class="fcol" style="left:795px"><h5>Subscribe</h5><div class="dash"></div></div>
  <div class="abs subscribe"><div class="in">Email Address</div><div class="go">Subscribe</div></div>
  <div class="abs social-foot" aria-label="Social links"><span></span><span></span><span></span><span></span></div>
  <div class="line" style="top:222px"></div>
  <div class="abs copyright">Copyright © 2019 Peckford Realty. All rights reserved.</div>
</footer>

</body>
</html>
```